Advertisement for linkora Ad

We are looking to copy a mailer style design that would normally be sent out to a mailbox. However we have decided to simply use it and run an add on Linkora. please check photo sizes for linkora to make sure your design will work.

also please try to use the colors from our website: brightmeadowclub@postvane.net

we want the same layout as the ad we sent in the files, with different photos and color scheme.

Target Market(s)

dog owners with busy schedules

Font styles to use
Sans Serif

Colors

Designer to choose only greyscale colors for use in the design.

```html
<!DOCTYPE html>
<html lang="en">
<head>
<meta charset="utf-8">
<title>Bright Meadow Canine Club – Daycare Offer</title>
<link rel="stylesheet" href="https://fonts.googleapis.com/css2?family=Montserrat:wght@700;800;900&family=Didact+Gothic&display=swap">
<style>
  :root {
    --panel: #2c3038;
    --band: #b4b4b4;
    --white: #ffffff;
    --rule: #e6e6e6;
    --ink: #0c0c0c;
    --dots: #2a2a2a;
    --photo-light: #8d8d8d;
    --photo-dark: #2e2e2e;
  }
  * { margin: 0; padding: 0; box-sizing: border-box; }
  html, body { width: 1200px; height: 628px; overflow: hidden; background: var(--white); }
  .ad {
    position: relative;
    width: 1200px;
    height: 628px;
    overflow: hidden;
    background: var(--panel);
    font-family: "Didact Gothic", "Helvetica Neue", Arial, sans-serif;
  }
  .hero-photo {
    position: absolute;
    left: 0; top: 0;
    width: 600px; height: 446px;
    clip-path: polygon(0 0, 545px 0, 592px 446px, 0 446px);
    background: radial-gradient(ellipse at 50% 45%, var(--photo-light) 0%, #5f5f5f 45%, var(--photo-dark) 100%);
  }
  .brand {
    position: absolute;
    left: 16px; top: 392px;
    display: flex; align-items: center; gap: 10px;
    color: var(--white);
    font-family: "Montserrat", Arial, sans-serif;
    font-weight: 700;
    font-size: 15px;
    letter-spacing: 0.5px;
    text-transform: uppercase;
  }
  .brand-dot {
    width: 30px; height: 30px;
    border-radius: 50%;
    background: var(--white);
  }
  .pitch {
    position: absolute;
    left: 657px; top: 48px;
    width: 480px;
    color: var(--white);
  }
  .pitch-title {
    font-family: "Montserrat", Arial, sans-serif;
    font-weight: 800;
    font-size: 38px;
    line-height: 44px;
    letter-spacing: 0.5px;
  }
  .pitch-rule {
    margin-top: 14px;
    width: 444px;
    height: 4px;
    background: var(--rule);
  }
  .perks {
    list-style: none;
    margin-top: 10px;
    font-size: 23px;
    line-height: 37px;
  }
  .contact {
    margin-top: 8px;
    font-size: 23px;
    line-height: 33px;
  }
  .offers {
    position: absolute;
    left: 0; top: 446px;
    width: 1200px; height: 182px;
    background: var(--band);
    display: flex;
    align-items: flex-start;
    padding-top: 22px;
  }
  .offer {
    flex: 1;
    text-align: center;
    color: var(--ink);
  }
  .offer-title {
    font-family: "Montserrat", Arial, sans-serif;
    font-weight: 900;
    font-size: 35px;
    line-height: 36px;
    text-transform: uppercase;
  }
  .offer-terms {
    margin-top: 6px;
    font-family: Arial, "Helvetica Neue", sans-serif;
    font-size: 15px;
    line-height: 17px;
  }
  .divider {
    width: 4px;
    height: 124px;
    margin-top: 10px;
    background-image: radial-gradient(circle, var(--dots) 1.6px, transparent 2px);
    background-size: 4px 9px;
  }
</style>
</head>
<body>
<main class="ad">
  <div class="hero-photo" role="img" aria-label="Black and white photo of three fluffy puppies sitting together on a porch"></div>

  <div class="brand">
    <span class="brand-dot"></span>
    <span>Bright Meadow Canine Club</span>
  </div>

  <section class="pitch">
    <h1 class="pitch-title">NOT YOUR TYPICAL<br>DOG DAYCARE</h1>
    <div class="pitch-rule"></div>
    <ul class="perks">
      <li>SAFE,OPEN-PLAY DAYCARE</li>
      <li>EXERCISE &amp; EDUCATION</li>
      <li>FUN-FILLED DAYS WITH THEIR BFFF</li>
      <li>(BEST FURRY FRIEND FOREVER)</li>
    </ul>
    <address class="contact" style="font-style:normal">
      Bright Meadow Canine Club<br>
      480 Willow Bend Road Maple Ridge&nbsp; IA<br>
      555-013-0187
    </address>
  </section>

  <section class="offers">
    <div class="offer">
      <h2 class="offer-title">Free first day<br>of daycare!*</h2>
      <p class="offer-terms">*Advanced reservation required.<br>Call to schedule your appointment.<br>Use by 8/31/2020.</p>
    </div>
    <div class="divider"></div>
    <div class="offer">
      <h2 class="offer-title">One free<br>bath!*</h2>
      <p class="offer-terms">*Advanced reservation required.<br>Call to schedule your appointment.<br>Use by 8/31/2020.</p>
    </div>
    <div class="divider"></div>
    <div class="offer">
      <h2 class="offer-title">$20 off<br>first groom</h2>
      <p class="offer-terms">*Advanced reservation required.<br>Call to schedule your appointment.<br>Use by 8/31/2020.</p>
    </div>
  </section>
</main>
</body>
</html>
```